Digital Marketing Website Redesign, modern, fresh, dynamic

Hi there, we would like to freshen up our website and create a new dynamic look. We are a digital marketing agency who specialise in digital transformation in the form of creating websites for appointment bookings. Our clients are service businesses such as hairdressers, dentists and doctors who's patients need to book appointments with them.

Our company name is Plombek with the point being we can help increase your revenue curve by increasing your appointment bookings.

Our services include building the website, creating campaigns to drive traffic, increasing conversions and monitoring and reporting.

We are playing with a tagline of 'Step into your Digital Transformation' as we have a 5 step journey that customers can take with us getting them from zero to full appointment bookings.

Our current website is www.plomnbek-site.example

You can see a draft design that I mocked up on Canva here https://www.drawpadhub.example/design/QXT82LmnB7K/PoWz41kdRtGyvb_sxE_JNq/edit?utm_content=QXT82LmnB7K&utm_campaign=designshare&utm_medium=link2&utm_source=sharebutton

Also attached some other homepage ideas. In regard to photos we are open to ideas.

Please let if you need any more information to provide us with an initial design. Thanks million and I look forward to receiving fantastic designs :)

Marissa Tobler
Plombek

Target Market(s)

Appointment based businesses such as hairdressers, dentists, doctors

Industry/Entity Type

Marketing and Digital

Coding

Coded - Design and coding required

Number of Pages Required

1 page

Colors
0094D4
00A9DD
6FCCEA
C7EBF8
E9F6FB

Requirements
Must have
• Appointment booking CTA
Nice to have
• A website we like https://www.morwenhalbrook.example

```html
<!DOCTYPE html>
<html lang="en">
<head>
<meta charset="utf-8">
<title>Plombek – Digital Transformation Consultancy</title>
<link href="https://fonts.googleapis.com/css2?family=Poppins:wght@400;500;600;700&family=Roboto:wght@400;500;700&display=swap" rel="stylesheet">
<style>
:root{
  --navy:#23487a;
  --navy-dark:#1d3d69;
  --lime:#a2a81d;
  --lime-bright:#b3b91f;
  --ink:#222;
  --grey:#666;
  --nav:#3d4a5a;
  --star:#f5b50a;
  --white:#fff;
}
*{box-sizing:border-box;margin:0;padding:0}
html,body{width:1200px;height:3857px;overflow:hidden}
body{font-family:"Roboto",sans-serif;color:var(--ink);background:var(--white);position:relative}
section,header,footer{position:absolute;left:0;width:1200px}
.abs{position:absolute}
.heading{font-family:"Poppins",sans-serif;font-weight:700}
.pill{display:flex;align-items:center;justify-content:center;border-radius:30px;background:var(--lime);color:#fff;font-weight:700;font-size:13px;text-transform:uppercase;letter-spacing:.2px}

/* header */
.site-header{top:0;height:94px;background:#fff}
.brand{left:111px;top:26px;font-family:"Poppins",sans-serif;font-weight:700;font-size:32px;color:var(--navy)}
.brand-tagline{left:280px;top:23px;font-size:13px;color:var(--grey);line-height:21px}
.main-nav{left:495px;top:36px;display:flex;gap:24px;font-size:13px;color:var(--nav)}
.book-btn{left:880px;top:25px;width:208px;height:39px;box-shadow:0 4px 10px rgba(0,0,0,.2)}

/* hero */
.hero{top:94px;height:600px;background:var(--navy)}
.hero h1{left:186px;top:172px;font-size:40px;line-height:51px;color:#fff}
.hero p{left:187px;top:281px;width:440px;font-family:"Poppins",sans-serif;font-size:13.5px;line-height:21.5px;color:#fff}
.start-btn{left:189px;top:383px;width:137px;height:35px;font-family:"Poppins",sans-serif;font-size:12px}
.hero-visual{left:635px;top:26px}

/* stats */
.stats{top:694px;height:291px;background:var(--lime)}
.stat{top:41px;width:220px;text-align:center;color:#fff}
.stat .circle{width:118px;height:118px;border-radius:50%;background:#fff;margin:0 auto;display:flex;align-items:center;justify-content:center}
.stat .label{margin-top:20px;font-weight:700;font-size:16px}
.stat .num{margin-top:10px;font-family:"Poppins",sans-serif;font-weight:600;font-size:29px}

/* testimonials */
.why{top:985px;height:608px;background:#fff}
.section-title{width:1200px;text-align:center;font-size:38px}
.why .section-title{top:70px;color:var(--navy)}
.quote-card{top:148px;width:302px;height:365px;background:#fff;box-shadow:0 4px 18px rgba(0,0,0,.09);text-align:center;padding:0 28px}
.quote-card .mark{margin-top:40px;font-family:"Poppins",sans-serif;font-weight:700;font-size:80px;line-height:50px;height:42px;color:var(--lime)}
.quote-card h3{margin-top:14px;font-size:19px;line-height:26px;color:var(--navy)}
.quote-card p{margin-top:12px;font-size:13px;line-height:26px;color:var(--grey)}
.quote-card .stars{margin-top:10px;color:var(--star);font-size:16px;letter-spacing:5px}
.author{margin-top:10px;display:flex;align-items:center;gap:8px;text-align:left}
.avatar{width:56px;height:56px;border-radius:50%;background:linear-gradient(135deg,#8b6a58,#3a2f2c);flex:none}
.author b{display:block;font-family:"Poppins",sans-serif;font-weight:600;font-size:18px}
.author span{font-family:"Poppins",sans-serif;font-size:13px;color:var(--grey)}

/* steps */
.steps{top:1593px;height:629px;background:var(--navy)}
.steps .section-title{top:90px;color:#fff}
.step{top:174px;width:302px}
.step .frame{height:241px;background:var(--lime);border-radius:10px;position:relative}
.step .photo{position:absolute;left:24px;top:23px;width:247px;height:262px;border-radius:4px 4px 10px 10px}
.step h3{position:absolute;top:304px;width:302px;text-align:center;color:#fff;font-size:22px}
.arrow{top:304px;width:38px;height:38px;border-radius:50%;background:#1a3358;display:flex;align-items:center;justify-content:center}

/* team */
.team{top:2222px;height:750px;background:#fff}
.team h2{left:111px;top:86px;font-size:40px;color:var(--navy)}
.team .intro{left:386px;top:98px;width:710px;font-size:14px;line-height:26px;color:var(--grey)}
.member{width:300px;text-align:center}
.member svg{display:block;margin:0 auto}
.member b{display:block;margin-top:12px;font-weight:500;font-size:20px}
.member span{display:block;margin-top:4px;font-size:20px;color:var(--navy)}

/* pricing */
.pricing{top:2972px;height:646px;background:var(--lime)}
.pricing .section-title{top:78px;color:#fff;font-size:40px}
.pricing .sub{top:143px;width:1200px;text-align:center;color:#fff;font-size:14px;line-height:26px}
.plan{top:220px;width:289px;height:333px;background:#fff;border-radius:12px;padding:18px 19px}
.plan .head{height:92px;background:var(--navy);border-radius:10px;color:#fff;text-align:center;padding-top:24px;font-size:14px}
.plan .price{margin-top:8px;font-weight:700;font-size:18px}
.plan .price small{font-weight:400;font-size:14px}
.plan .item{margin-top:24px}
.plan .item + .item{margin-top:16px}
.plan .item b{display:block;font-size:17px;color:var(--navy);font-weight:700}
.plan .item span{display:block;margin-top:6px;font-size:12.5px;line-height:20px;color:var(--grey)}
.plan .pill{position:absolute;left:22px;bottom:28px;width:240px;height:37px;font-size:13px}

/* footer */
.site-footer{top:3618px;height:239px;background:var(--navy);color:#fff}
.footer-brand{left:111px;top:80px;font-family:"Poppins",sans-serif;font-weight:700;font-size:56px}
.footer-links{font-size:13px;line-height:25px}
.footer-contact{font-size:13px;line-height:25px}
.footer-rule{left:491px;top:127px;width:597px;height:1px;background:rgba(255,255,255,.6)}
.copyright{right:112px;top:168px;font-size:14px}
</style>
</head>
<body>

<header class="site-header">
  <div class="abs brand">Plombek</div>
  <div class="abs brand-tagline">Digital Transformation<br>Consultancy</div>
  <nav class="abs main-nav"><span>5 steps</span><span>Our Pricing</span><span>Ahead of the Curve</span><span>Our Team</span></nav>
  <div class="abs pill book-btn">Book an appointment</div>
</header>

<section class="hero">
  <h1 class="abs heading">Step into your<br>Digital Transformation</h1>
  <p class="abs">Digital transformation is a journey. At Plombek we divide the journey into five key steps that take your business from comprehensive market research to full appointment bookings. Ready to go on that journey?</p>
  <div class="abs pill start-btn">Start here</div>
  <svg class="abs hero-visual" width="565" height="574" viewBox="0 0 565 574" role="img" aria-label="Photo of a person walking into a glowing blue digital tunnel">
    <defs>
      <radialGradient id="tunnel" cx="0.48" cy="0.45" r="0.6">
        <stop offset="0" stop-color="#e6fbff"/>
        <stop offset="0.25" stop-color="#4fd3f2"/>
        <stop offset="0.6" stop-color="#1479b8"/>
        <stop offset="1" stop-color="#0b2b57"/>
      </radialGradient>
    </defs>
    <path d="M120 10 C200 -8 320 0 420 10 C500 18 560 40 565 90 L565 574 L40 574 C10 520 -8 430 20 360 C40 300 10 260 20 200 C30 120 60 30 120 10 Z" fill="url(#tunnel)"/>
  </svg>
</section>

<section class="stats">
  <div class="abs stat" style="left:124px">
    <div class="circle"><svg width="60" height="60" viewBox="0 0 60 60" fill="none" stroke="#23487a" stroke-width="2"><rect x="6" y="10" width="38" height="38" rx="3"/><line x1="6" y1="20" x2="44" y2="20"/><line x1="15" y1="5" x2="15" y2="14"/><line x1="35" y1="5" x2="35" y2="14"/><line x1="12" y1="28" x2="30" y2="28"/><line x1="12" y1="36" x2="26" y2="36"/><circle cx="44" cy="44" r="10" stroke="#a2a81d"/><path d="M39 44l4 4 7-7" stroke="#a2a81d"/></svg></div>
    <div class="label">Appointments Booked</div><div class="num">762</div>
  </div>
  <div class="abs stat" style="left:368px">
    <div class="circle"><svg width="60" height="60" viewBox="0 0 60 60" fill="none" stroke="#23487a" stroke-width="2"><rect x="6" y="16" width="26" height="20" rx="4"/><path d="M14 36l-3 7 9-7"/><rect x="28" y="6" width="26" height="20" rx="4" stroke="#a2a81d"/><path d="M12 22h14M12 28h10"/><path d="M36 20v-6h4l3-4v10z" stroke="#a2a81d"/><circle cx="30" cy="48" r="6"/></svg></div>
    <div class="label">Marketing Campaigns</div><div class="num">31</div>
  </div>
  <div class="abs stat" style="left:612px">
    <div class="circle"><svg width="60" height="60" viewBox="0 0 60 60" fill="none" stroke="#23487a" stroke-width="2"><rect x="6" y="8" width="48" height="34" rx="3"/><line x1="6" y1="16" x2="54" y2="16"/><path d="M24 24l-6 5 6 5M36 24l6 5-6 5M32 22l-4 14" stroke="#a2a81d"/><path d="M24 42l-3 10h18l-3-10M18 52h24"/></svg></div>
    <div class="label">Website Traffic Increase</div><div class="num">25%</div>
  </div>
  <div class="abs stat" style="left:857px">
    <div class="circle"><svg width="60" height="60" viewBox="0 0 60 60" fill="none" stroke="#23487a" stroke-width="2"><circle cx="32" cy="20" r="10" stroke="#a2a81d"/><path d="M28 30v5h8v-5" stroke="#a2a81d"/><path d="M32 4v-2M18 8l-2-2M46 8l2-2M14 20h-3M50 20h3" stroke="#a2a81d"/><path d="M6 44h10l10 4h12c3 0 3 4 0 4H26M16 54l14 2 22-10c3-2 1-5-2-4l-12 4"/></svg></div>
    <div class="label">Creative Ideas</div><div class="num">762</div>
  </div>
</section>

<section class="why">
  <h2 class="abs heading section-title">Why others choose us?</h2>
  <article class="abs quote-card" style="left:111px">
    <div class="mark">“</div>
    <h3 class="heading">100 bookings in<br>first month!</h3>
    <p>Plombek’s booking system helped us get over 100 appointment bookings in May 2020.</p>
    <div class="stars">★★★★★</div>
    <div class="author"><div class="avatar" role="img" aria-label="Portrait of the client"></div><div><b>Lorena Vasquel</b><span>Owner, Shear &amp; Shine</span></div></div>
  </article>
  <article class="abs quote-card" style="left:449px">
    <div class="mark">“</div>
    <h3 class="heading">From 55 new patients<br>per month!</h3>
    <p>Since Plombek optimised our marketing campaigns we’ve had 55-75 new patients per month.</p>
    <div class="stars">★★★★★</div>
    <div class="author"><div class="avatar" role="img" aria-label="Portrait of the client"></div><div><b>Dr. Haneul Park</b><span>Owner, Brightbite Dental</span></div></div>
  </article>
  <article class="abs quote-card" style="left:786px">
    <div class="mark">“</div>
    <h3 class="heading">25% increase in<br>web traffic!</h3>
    <p>Plombek have increased our SiteRank ranking by 20,000 and our web traffic by 25%</p>
    <div class="stars">★★★★★</div>
    <div class="author"><div class="avatar" role="img" aria-label="Portrait of the client"></div><div><b>Ansel Wrobek</b><span>CEO, LedgerPulse</span></div></div>
  </article>
</section>

<section class="steps">
  <h2 class="abs heading section-title">5 Steps</h2>
  <div class="abs arrow" style="left:37px"><svg width="10" height="12" viewBox="0 0 10 12"><path d="M7 1L2 6l5 5" stroke="#fff" stroke-width="2" fill="none"/></svg></div>
  <div class="abs arrow" style="left:1125px"><svg width="10" height="12" viewBox="0 0 10 12"><path d="M3 1l5 5-5 5" stroke="#fff" stroke-width="2" fill="none"/></svg></div>
  <div class="abs step" style="left:111px">
    <div class="frame"><div class="photo" role="img" aria-label="Photo of a hand placing a glowing light bulb on wooden blocks" style="background:linear-gradient(160deg,#c9bfb6,#8a6a52 55%,#3e3530)"></div></div>
    <h3 class="heading">Creative campaigns</h3>
  </div>
  <div class="abs step" style="left:449px">
    <div class="frame"><div class="photo" role="img" aria-label="Photo of two colleagues reviewing research at a laptop" style="background:linear-gradient(160deg,#e4e6e8,#9aa3a8 55%,#4b5560)"></div></div>
    <h3 class="heading">Market Research</h3>
  </div>
  <div class="abs step" style="left:786px">
    <div class="frame"><div class="photo" role="img" aria-label="Photo of a person booking online at a desktop computer" style="background:linear-gradient(160deg,#f1f0ee,#c8c6c2 55%,#7a756e)"></div></div>
    <h3 class="heading">Online Bookings</h3>
  </div>
</section>

<section class="team">
  <h2 class="abs heading">Our Team</h2>
  <p class="abs intro">From business management and web development to creative campaign delivery and social media expertise, our team has all the experience your business needs to it to the top of its digital game.</p>
  <div class="abs member" style="left:124px;top:180px"><svg width="124" height="138" viewBox="0 0 124 138" role="img" aria-label="Portrait photo of Ronan"><path d="M62 0L124 34V104L62 138 0 104V34Z" fill="#b9a999"/></svg><b>Ronan</b><span>Account Manager</span></div>
  <div class="abs member" style="left:450px;top:180px"><svg width="124" height="138" viewBox="0 0 124 138" role="img" aria-label="Portrait photo of Callum"><path d="M62 0L124 34V104L62 138 0 104V34Z" fill="#c9c9c9"/></svg><b>Callum</b><span>Account Manager</span></div>
  <div class="abs member" style="left:776px;top:180px"><svg width="124" height="138" viewBox="0 0 124 138" role="img" aria-label="Portrait photo of Mira"><path d="M62 0L124 34V104L62 138 0 104V34Z" fill="#a9d6e0"/></svg><b>Mira</b><span>Website specialist</span></div>
  <div class="abs member" style="left:124px;top:420px"><svg width="124" height="138" viewBox="0 0 124 138" role="img" aria-label="Portrait photo of Sahana"><path d="M62 0L124 34V104L62 138 0 104V34Z" fill="#d8d4d0"/></svg><b>Sahana</b><span>Web developer</span></div>
  <div class="abs member" style="left:450px;top:420px"><svg width="124" height="138" viewBox="0 0 124 138" role="img" aria-label="Portrait photo of Maeve"><path d="M62 0L124 34V104L62 138 0 104V34Z" fill="#3f6a4e"/></svg><b>Maeve</b><span>Content Creator</span></div>
  <div class="abs member" style="left:776px;top:420px"><svg width="124" height="138" viewBox="0 0 124 138" role="img" aria-label="Portrait photo of Lucia"><path d="M62 0L124 34V104L62 138 0 104V34Z" fill="#5a5f66"/></svg><b>Lucia</b><span>Social media specialist</span></div>
</section>

<section class="pricing">
  <h2 class="abs heading section-title">Our Pricing</h2>
  <p class="abs sub">Which plan you take will depend on how many steps you want to take on<br>your digital transformation journey.</p>
  <div class="abs plan" style="left:111px">
    <div class="head">Starter Plan<div class="price">€399 <small>&nbsp;/a month</small></div></div>
    <div class="item"><b>Step 1:</b><span>Online readiness review based on our 12 point checklist</span></div>
    <div class="item"><b>Step 2:</b><span>Implementation</span></div>
    <div class="pill">Take 2 steps</div>
  </div>
  <div class="abs plan" style="left:455px">
    <div class="head">Premium Plan<div class="price">€599 <small>&nbsp;/a month</small></div></div>
    <div class="item"><b>Step 1:</b><span>Steps 1, 2 &amp; 3</span></div>
    <div class="item" style="margin-top:36px"><b>Step 3:</b><span>Content is King</span></div>
    <div class="pill">Take 3 steps</div>
  </div>
  <div class="abs plan" style="left:799px">
    <div class="head">Ultimate Plan<div class="price">€899 <small>&nbsp;/a month</small></div></div>
    <div class="item"><b>Step 4:</b><span>Marketing Campaign</span></div>
    <div class="item" style="margin-top:36px"><b>Step 5:</b><span>Implementation</span></div>
    <div class="pill">Take the full journey</div>
  </div>
</section>

<footer class="site-footer">
  <div class="abs footer-brand">Plombek</div>
  <div class="abs footer-links" style="left:494px;top:58px">5 steps<br>Our Pricing</div>
  <div class="abs footer-links" style="left:624px;top:58px">Ahead of the Curve<br>Our Team</div>
  <div class="abs footer-contact" style="left:790px;top:58px">
    <svg width="10" height="13" viewBox="0 0 10 13" style="margin-right:6px"><path d="M5 0a5 5 0 0 0-5 5c0 4 5 8 5 8s5-4 5-8a5 5 0 0 0-5-5z" fill="#a2a81d"/><circle cx="5" cy="5" r="2" fill="#23487a"/></svg>Co. Westmarra<br><span style="padding-left:18px">Ireland X00 Q1ZZ</span>
  </div>
  <div class="abs footer-contact" style="left:953px;top:58px">
    <svg width="13" height="10" viewBox="0 0 13 10" style="margin-right:6px"><rect width="13" height="10" rx="1" fill="#a2a81d"/><path d="M0 1l6.5 5L13 1" stroke="#23487a" fill="none"/></svg>info@plombek.example<br>
    <svg width="12" height="12" viewBox="0 0 12 12" style="margin-right:7px"><path d="M2 0l3 3-1.5 2a7 7 0 0 0 3.5 3.5L9 7l3 3-2 2C5 12 0 7 0 2z" fill="#a2a81d"/></svg>+353 1 555 0142
  </div>
  <div class="abs footer-rule"></div>
  <div class="abs copyright">2024 Copyright - &nbsp;Company name &nbsp;| All Rights Reserved</div>
</footer>

</body>
</html>
```